St Louis Electrician Needing a Business Card Design!!

We are a St Louis based electrical contracting firm that needs help designing a business card. We have a logo and I have another image that I would like to incorporate. Open to ideas..Thanks!!

Industry/Entity Type

Business

Requirements
Must have
• there are two downloads...one is the logo and the other is what i was wanting coming off the logo...the light rays. Like the logo with the blue background...Was thinking the whole card would be that color blue.
Should not have
• No lightning bolts

```html
<!DOCTYPE html>
<html lang="en">
<head>
<meta charset="utf-8">
<title>Voltmark Inc. Business Card</title>
<link href="https://fonts.googleapis.com/css2?family=Source+Sans+3:wght@400;600;700&display=swap" rel="stylesheet">
<style>
  :root {
    --brand-blue: #0a52a8;
    --ink: #1d1d1f;
    --card: #ffffff;
    --backdrop: #e9e7e5;
  }
  html, body {
    margin: 0;
    padding: 0;
    width: 1200px;
    height: 900px;
    overflow: hidden;
    background: var(--backdrop);
    font-family: "Source Sans 3", sans-serif;
  }
  .canvas {
    position: relative;
    width: 1200px;
    height: 900px;
  }
  .card {
    position: absolute;
    background: var(--card);
    border-radius: 18px;
    overflow: hidden;
    box-shadow: 0 6px 18px rgba(0,0,0,0.12);
  }
  .card-front {
    left: 78px;
    top: 35px;
    width: 588px;
    height: 362px;
  }
  .brand-band {
    position: absolute;
    left: 65px;
    top: 0;
    width: 137px;
    height: 100%;
    background: var(--brand-blue);
  }
  .brand-band .brand-name {
    position: absolute;
    left: 50%;
    bottom: 40px;
    writing-mode: vertical-rl;
    transform: translateX(-50%) rotate(180deg);
    color: #ffffff;
    font-size: 31px;
    font-weight: 400;
    letter-spacing: 0.5px;
    white-space: nowrap;
  }
  .contact-block {
    position: absolute;
    left: 262px;
    top: 100px;
    color: var(--ink);
  }
  .person-name {
    margin: 0;
    color: var(--brand-blue);
    font-size: 23px;
    font-weight: 700;
    line-height: 1.1;
  }
  .person-role {
    margin: 3px 0 0;
    font-size: 16px;
  }
  .address {
    margin: 16px 0 0;
    font-size: 16px;
    line-height: 21px;
    font-style: normal;
  }
  .contact-list {
    list-style: none;
    margin: 14px 0 0;
    padding: 0;
    font-size: 16px;
    line-height: 21px;
  }
  .contact-list li {
    display: flex;
    align-items: center;
    gap: 9px;
  }
  .contact-list svg {
    width: 13px;
    height: 13px;
    fill: var(--brand-blue);
    flex: none;
  }
  .card-back {
    left: 390px;
    top: 507px;
    width: 564px;
    height: 348px;
  }
  .back-brand {
    position: absolute;
    left: 92px;
    top: 150px;
    display: flex;
    align-items: center;
    gap: 12px;
    color: var(--brand-blue);
    font-size: 40px;
    font-weight: 400;
    white-space: nowrap;
  }
  .back-brand .mark {
    width: 16px;
    height: 16px;
    border-radius: 50%;
    background: var(--brand-blue);
  }
</style>
</head>
<body>
<div class="canvas">
  <section class="card card-front">
    <div class="brand-band">
      <span class="brand-name">Voltmark Inc.</span>
    </div>
    <div class="contact-block">
      <h1 class="person-name">Daniel Morrow</h1>
      <p class="person-role">Managing Director</p>
      <address class="address">4870 Harlow Street<br>Brookvale, 630118.</address>
      <ul class="contact-list">
        <li>
          <svg viewBox="0 0 16 16"><path d="M3.6 1.2l2.3 2.6-1.2 1.8c.9 2 2.5 3.6 4.6 4.6l1.8-1.2 2.6 2.3-1.3 2.3C6.8 13.5 2.5 9.2 1.3 3.9z"/></svg>
          055-318 742 610
        </li>
        <li>
          <svg viewBox="0 0 16 16"><path d="M1 3h14v10H1z M2 4.2v.4l6 4 6-4v-.4z" fill-rule="evenodd"/></svg>
          hello@voltmark.com
        </li>
        <li>
          <svg viewBox="0 0 16 16"><path d="M6.5 9.5l3-3 1 1-3 3z M4 8.5l2-2 1 1-2 2a1.4 1.4 0 002 2l2-2 1 1-2 2a2.8 2.8 0 01-4-4z M12 7.5l-2 2-1-1 2-2a1.4 1.4 0 00-2-2l-2 2-1-1 2-2a2.8 2.8 0 014 4z"/></svg>
          www.voltmarkinc.com
        </li>
      </ul>
    </div>
  </section>

  <section class="card card-back">
    <div class="back-brand">
      <span class="mark"></span>
      <span>Voltmark Inc.</span>
    </div>
  </section>
</div>
</body>
</html>
```